pathology learning flashcard template graphic design .

Creative designs for 2 sides of the flashcards to include colorful sectioning and font sizes that will make it easy to use in studying.

```html
<!DOCTYPE html>
<html lang="en">
<head>
<meta charset="utf-8">
<title>Pathology Flashcard – Gastrointestinal Case 0001</title>
<link href="https://fonts.googleapis.com/css2?family=Arimo:ital,wght@0,400;0,700;1,400;1,700&family=Roboto+Condensed:ital,wght@0,400;0,700;1,400;1,700&display=swap" rel="stylesheet">
<style>
  :root{
    --red:#e41e20;
    --pink:#f6cfd0;
    --white:#ffffff;
    --ink:#1d1d1b;
    --canvas:#ffffff;
  }
  *{box-sizing:border-box;margin:0;padding:0}
  html,body{width:1200px;height:1200px;overflow:hidden;background:var(--canvas)}
  body{position:relative;font-family:"Arimo",Arial,sans-serif;color:var(--ink)}

  .card{position:absolute;left:364px;width:453px;height:311px;overflow:hidden}
  .card--front{top:144px;background:var(--white)}
  .card--back{top:792px;background:var(--red)}

  /* front */
  .front-header{position:absolute;left:0;top:0;width:453px;height:120px;background:var(--red)}
  .system-title{position:absolute;left:11px;top:39px;font-size:21.5px;font-weight:700;color:var(--white);letter-spacing:.2px}
  .header-rule{position:absolute;left:0;top:69px;width:317px;height:1.5px;background:var(--white)}
  .case-id{position:absolute;left:11px;top:88px;font-size:14.5px;font-style:italic;font-weight:700;color:var(--white);letter-spacing:-.2px}
  .organ-art{position:absolute;left:317px;top:0;width:120px;height:120px;
    background:radial-gradient(ellipse at 50% 60%,#e88a8e 0%,#c9646a 45%,#7a4a38 80%,#b9835f 100%)}
  .case-text{position:absolute;left:0;top:120px;width:290px;height:168px;background:var(--pink);
    padding:8px 8px 0 11px;font-size:10.8px;line-height:15.1px;letter-spacing:-.15px}
  .question{position:absolute;left:290px;top:120px;width:163px;height:168px;padding:10px 13px;border-right:1px solid var(--pink)}
  .question-title{color:var(--red);font-weight:700;font-size:11.2px;line-height:15.5px}
  .options{list-style:none;margin-top:13px;font-size:10px;font-weight:700;line-height:13.5px}
  .front-footer{position:absolute;left:0;top:288px;width:453px;height:23px;background:var(--red)}

  /* back */
  .answer-notes{position:absolute;left:0;top:0;width:453px;height:211px;padding:10px 22px 0 11px;color:var(--white);font-family:"Roboto Condensed",sans-serif}
  .disease-title{font-family:"Arimo",sans-serif;font-style:italic;font-weight:700;font-size:14.5px;margin-bottom:4px}
  .note{font-size:7.4px;font-style:italic;line-height:10.4px;margin-bottom:16px}
  .note-label{font-size:10px;font-weight:400}
  .explanation{position:absolute;left:0;top:211px;width:453px;height:75px;background:var(--pink);padding:10px 20px 0 11px;font-family:"Roboto Condensed",sans-serif;font-style:italic}
  .explanation h3{font-size:10px;font-weight:700;line-height:12px}
  .explanation p{font-size:7.3px;line-height:10.4px}
  .back-footer{position:absolute;left:0;top:286px;width:453px;height:25px;display:flex;align-items:center;justify-content:space-between;padding:0 12px;color:var(--white);font-family:"Roboto Condensed",sans-serif}
  .sources{font-size:6.4px}
  .page-number{font-size:11px}
</style>
</head>
<body>

<section class="card card--front">
  <div class="front-header">
    <h1 class="system-title">GASTROINTESTINAL</h1>
    <div class="header-rule"></div>
    <h2 class="case-id">PATHOLOGY CASE ID 0001</h2>
    <div class="organ-art" role="img" aria-label="Illustration of human abdominal organs: kidneys, intestines and bladder"></div>
  </div>
  <div class="case-text">50-year-old woman comes to the clinic because she has difficulty swallowing for the past few months. She says symptoms have been worsening. She also complains of cough, mostly at night and in fear of choking, has stopped eating many foods, losing about 12 lbs in the past 3 months.&nbsp; Past medical history is unremarkable. Vital signs are normal and physical exam is unremarkable. Chest x-ray with demonstrates an air-fluid level, while manometry shows absent relaxation of the lower esophageal sphincter during swallowing.</div>
  <div class="question">
    <p class="question-title">What is the most likely diagnosis?</p>
    <ul class="options">
      <li>A) GERD</li>
      <li>B) Barret Esophagus</li>
      <li>C) Achalasia</li>
      <li>D) Eosinophilic esophagitis</li>
    </ul>
  </div>
  <div class="front-footer"></div>
</section>

<section class="card card--back">
  <div class="answer-notes">
    <h2 class="disease-title">Achalasia</h2>
    <p class="note"><span class="note-label">Definition:</span> •Motility disorder where esophageal relaxation is impaired in the lower esophageal sphincter (LES).</p>
    <p class="note"><span class="note-label">Etiology/Pathology:</span> Destruction of inhibitory neurons in the Auerbach plexus.&nbsp; Loss of peristalsis in the lower esophageal sphincter (Lower-two thirds of the esophagus).</p>
    <p class="note"><span class="note-label">P/E and Symptoms:</span> Dysphagia that is progressive, regurgitation, weight-loss, dry cough, chest pain, GERD, esophageal perforation, squamous cell carcinoma, aspiration pneumonia.</p>
    <p class="note"><span class="note-label">Dx:</span> Barium swallow will show ‘bird’s beak’ and esophageal dilation.&nbsp; Manometry will present with increased resting lower esophageal sphincter pressure. Endoscopy will usually present with normal mucosa and LES dilation, and in some cases residual material such as undigested food particles may be present.</p>
    <p class="note"><span class="note-label">Rx:</span> First line of treatment are nitrates, calcium channel blockers, and Botulinum toxin injection in the LES.&nbsp; Long term management options include esophageal dilation with pneumatic balloon and myotomy.</p>
  </div>
  <div class="explanation">
    <h3>C- Achalasia</h3>
    <p>Symptoms and studies suggestive of achalasia.&nbsp; Patient’s manometry presents with no relaxation of the lower esophageal sphincter during swallowing.&nbsp; Patient also complains of dysphagia and is unable to swallow properly, leading to weight loss.&nbsp; Patient has no past infection or inflammation, ruling out eosinophilic esophagitis.&nbsp; Patient does not have chronic GERD, eliminating the possibility of Barrett esophagus, in which at least 5 years of acid reflux are beforehand to develop columnar metaplasia.</p>
  </div>
  <div class="back-footer">
    <span class="sources">Sources: Clinical Drug Handbook; Pocket Pharmacology Guide; MedRefOnline.example; ClinicalNotes.example</span>
    <span class="page-number">1</span>
  </div>
</section>

</body>
</html>
```